Software Company Banner Ad

We need a banner ad in two sizes. 728x90 and 300x250.
They should have strong similarity to the following ads:
http://www.vexlo.net/search/results?brand[0]=quorp&ad=4821396
http://www.vexlo.net/search/results?brand[0]=dravensoft&ad=4830517
Idea will be very similar. We want the same grey color, white text, and a realistic owl that blinks. The owl should have dramatic, bright, yellow eyes. The text will animate "from the top" as in the example. Though the logo animation will be different, all text and non-logo animation should match the animation in the example advertisements. The text will rotate between the following four sentences and images.
Looking for a provider of procurement cloud apps?
[Images - attached below]
The experts really liked our KTV booth.
Get great results with every procurement. [Learn more]
There are three vector files attached below. Feel free to change the colors as necessary to match the color scheme of the ad. We need one 2013 and one 2014 award in the ad.
The awards could appear simultaneously, could swap with each other or could appear in succession. Animation is acceptable.
There is an additional vector file with the company logo. The company logo should go where the Quorp logo is in horizontal ad. The company logo should go where the Dravensoft logo is in the block ad. The example ad has two logos. We will only need one logo on our ads. The logo should be changed to the color of the text used for the ad (white).
The owls eyes should slowly blink two times (as in the example).
The owl eyes should immediately grab someone's attention and all colors should compliment these eyes.
The [Learn more] button should have animation. The button should match the color of the owl's eyes. There should be a line/gleam/glare of light that travels across the button. The button should be embossed with the subtle animation occurring each time it appears.
Ads should be done with flash. We will need the source files and the names of any fonts used at the end of the project.
Thank you and please do not hesitate to contact with any questions.
Reason: We have contacted several photographers to see if the alternative owl images are available on Pixvane, Framelodge or similar. The duration extension is to accommodate this.
Target Market(s)
Target customers are procurement department employees of large companies.
Industry/Entity Type
It Company

```html
<!DOCTYPE html>
<html lang="en">
<head>
<meta charset="utf-8">
<title>Quorp · Veltrix Procurement Banner</title>
<link rel="stylesheet" href="https://fonts.googleapis.com/css2?family=Arimo:wght@400;700&display=swap">
<style>
  :root {
    --bg-grey: #4b4b4b;
    --bg-grey-dark: #2f2f2f;
    --topbar: #3a3a3a;
    --text-white: #ffffff;
    --badge-white: #f4f4f4;
    --badge-red: #d9432b;
    --badge-orange: #f08a24;
    --button-top: #ffd21a;
    --button-bottom: #f2a900;
    --button-edge: #b37a00;
    --button-text: #2a2200;
    --scene-dark: #1b1b1b;
    --scene-mid: #6e6c68;
    --scene-light: #c9c6bf;
    --scene-pale: #e6e3dc;
  }
  html, body {
    margin: 0;
    padding: 0;
    overflow: hidden;
    background: #ffffff;
  }
  .banner {
    position: relative;
    width: 1200px;
    height: 148px;
    overflow: hidden;
    background: linear-gradient(90deg, var(--bg-grey) 0%, #555555 40%, var(--bg-grey-dark) 60%);
    font-family: "Arimo", Arial, sans-serif;
    color: var(--text-white);
  }
  .brand-bar {
    position: absolute;
    left: 0;
    top: 0;
    width: 182px;
    height: 34px;
    background: var(--topbar);
    display: flex;
    align-items: center;
    gap: 12px;
    padding-left: 10px;
    box-sizing: border-box;
  }
  .brand {
    display: flex;
    align-items: center;
    gap: 6px;
    font-size: 17px;
    font-weight: 700;
    color: var(--text-white);
    letter-spacing: 0.3px;
  }
  .brand-mark {
    width: 11px;
    height: 11px;
    background: var(--text-white);
  }
  .brand-divider {
    width: 1px;
    height: 20px;
    background: #777777;
  }
  .headline {
    position: absolute;
    left: 118px;
    top: 54px;
    width: 340px;
    margin: 0;
    text-align: center;
    font-size: 29px;
    font-weight: 400;
    line-height: 36px;
    color: var(--text-white);
    white-space: nowrap;
  }
  .award {
    position: absolute;
    top: 18px;
    width: 62px;
    height: 60px;
  }
  .award--2013 { left: 496px; }
  .award--2014 { left: 574px; }
  .cta {
    position: absolute;
    left: 511px;
    top: 98px;
    width: 115px;
    height: 33px;
    border-radius: 4px;
    border: 1px solid var(--button-edge);
    background: linear-gradient(180deg, var(--button-top) 0%, var(--button-bottom) 100%);
    box-shadow: inset 0 1px 0 rgba(255,255,255,0.6), 0 1px 2px rgba(0,0,0,0.5);
    color: var(--button-text);
    font-size: 16px;
    font-weight: 700;
    display: flex;
    align-items: center;
    justify-content: center;
    box-sizing: border-box;
  }
  .owl-scene {
    position: absolute;
    left: 660px;
    top: 0;
    width: 540px;
    height: 148px;
    background:
      radial-gradient(ellipse 120px 90px at 320px 30px, var(--scene-pale) 0%, var(--scene-light) 40%, transparent 100%),
      radial-gradient(ellipse 200px 150px at 320px 120px, var(--scene-light) 0%, var(--scene-mid) 50%, transparent 100%),
      linear-gradient(90deg, var(--scene-dark) 0%, #3a3a39 25%, #4d4c4a 55%, #5a5955 80%, #3a3a38 100%);
  }
</style>
</head>
<body>
  <div class="banner">
    <div class="brand-bar">
      <div class="brand"><span class="brand-mark"></span>Quorp</div>
      <span class="brand-divider"></span>
      <div class="brand">Veltrix</div>
    </div>

    <p class="headline">Get great results<br>with every procurement!</p>

    <svg class="award award--2013" viewBox="0 0 64 60" aria-hidden="true">
      <rect x="4" y="0" width="56" height="44" rx="2" fill="var(--badge-white)"/>
      <rect x="4" y="30" width="56" height="8" fill="var(--badge-red)"/>
      <polygon points="0,40 64,40 58,48 64,56 0,56 6,48" fill="var(--badge-orange)"/>
    </svg>
    <svg class="award award--2014" viewBox="0 0 64 60" aria-hidden="true">
      <rect x="4" y="0" width="56" height="44" rx="2" fill="var(--badge-white)"/>
      <rect x="4" y="30" width="56" height="8" fill="var(--badge-red)"/>
      <polygon points="0,40 64,40 58,48 64,56 0,56 6,48" fill="var(--badge-orange)"/>
    </svg>

    <div class="cta">learn more&gt;</div>

    <div class="owl-scene" role="img" aria-label="Photograph of a grey owl with bright yellow eyes against dark forest trees"></div>
  </div>
</body>
</html>
```